Corporate Notepads

We currently have a basic notepad with our logo and icon at the top along with contact information at the bottom. We want to come up with something more creative and jazz it up a bit. We are looking for unique ideas to make the notepads look nice and corporate possibly with watermarked look. We will take any ideas and choose the one that works best for the look. We have a website where you can get ideas about our company. Attached is the current simple notepad design we have right now.

```html
<!DOCTYPE html>
<html lang="en">
<head>
<meta charset="utf-8">
<title>Harlow Construction – Notepad</title>
<link href="https://fonts.googleapis.com/css2?family=Oswald:wght@400;500;600&display=swap" rel="stylesheet">
<style>
  :root {
    --backdrop: #eeeeee;
    --paper: #f4f4f4;
    --navy: #2b3c8c;
    --ink: #111111;
    --concrete-light: #d6d6d6;
    --concrete-dark: #b9b9b9;
    --watermark: #e2e2e6;
    --white: #ffffff;
  }
  * { margin: 0; padding: 0; box-sizing: border-box; }
  html, body { width: 1200px; height: 795px; overflow: hidden; }
  body {
    background: var(--backdrop);
    font-family: "Oswald", "Arial Narrow", sans-serif;
    position: relative;
  }
  .notepad-sheet {
    position: absolute;
    left: 320px; top: 24px;
    width: 560px; height: 747px;
    background: var(--paper);
    box-shadow: 0 2px 10px rgba(0,0,0,.12);
    overflow: hidden;
  }
  .header-concrete {
    position: absolute; left: 0; top: 0;
    width: 100%; height: 96px;
    background: radial-gradient(circle at 30% 40%, var(--concrete-light), var(--concrete-dark));
  }
  .header-rules { position: absolute; left: 0; top: 0; }
  .brand-block {
    position: absolute; left: 22px; top: 40px;
    display: flex; align-items: center; gap: 8px;
  }
  .brand-square {
    width: 34px; height: 34px; background: var(--navy);
  }
  .brand-name {
    color: var(--navy); font-weight: 600; font-size: 30px;
    line-height: 1; letter-spacing: .5px;
  }
  .brand-sub {
    position: absolute; left: 64px; top: 74px;
    font-size: 9px; color: var(--ink); letter-spacing: .6px;
  }
  .brand-tagline {
    position: absolute; left: 22px; top: 84px;
    font-size: 8px; color: var(--ink); letter-spacing: .4px;
  }
  .header-mark {
    position: absolute; right: 40px; top: 18px;
    width: 62px; height: 62px; background: var(--ink);
  }
  .watermark-name {
    position: absolute; left: 0; right: 0; top: 360px;
    text-align: center;
    font-size: 150px; font-weight: 600; letter-spacing: 4px;
    color: var(--watermark);
  }
  .footer-band {
    position: absolute; left: 0; bottom: 28px;
    width: 486px; height: 38px;
    background: var(--navy); color: var(--white);
    display: flex; align-items: center; justify-content: space-between;
    padding: 0 16px;
  }
  .footer-services { font-size: 17px; font-weight: 500; letter-spacing: .3px; }
  .footer-contact { display: flex; gap: 22px; font-size: 12px; letter-spacing: .3px; }
  .footer-corner {
    position: absolute; right: 18px; bottom: 46px;
    width: 44px; height: 44px; background: var(--ink);
  }
</style>
</head>
<body>
  <main class="notepad-sheet">
    <div class="header-concrete" role="img" aria-label="Grey concrete texture header strip"></div>
    <svg class="header-rules" width="560" height="110" viewBox="0 0 560 110">
      <line x1="0" y1="104" x2="560" y2="96" stroke="var(--navy)" stroke-width="3"/>
      <line x1="330" y1="99" x2="560" y2="92" stroke="var(--ink)" stroke-width="3"/>
    </svg>
    <div class="brand-block">
      <span class="brand-square"></span>
      <span class="brand-name">HARLOW</span>
    </div>
    <div class="brand-sub">CONSTRUCTION</div>
    <div class="brand-tagline">CIVIL • INDUSTRIAL • COMMERCIAL</div>
    <div class="header-mark"></div>

    <div class="watermark-name">HARLOW</div>

    <div class="footer-corner"></div>
    <footer class="footer-band">
      <span class="footer-services">CIVIL • INDUSTRIAL • COMMERCIAL</span>
      <span class="footer-contact">
        <span>www.harlowbuilds.com</span>
        <span>555.014.2290</span>
      </span>
    </footer>
  </main>
</body>
</html>
```